Attic Rivers (Progressive House Album)

Hey Guys,

I'm a music artist and I need a CD Cover done for my new album.The album is called "Attic Rivers" and I really need something artistic, almost like a painting that reflects the name of the album.

Also please feel free to step out from the whole "almost like a painting" box, if your inner creator has something else to say. But preferably I'd have it as a painting...

Here are some keywords: Deep, Progressive, Lucid Dreaming, Ocean, Bedroom...

Please listen to the 3:30 demo of the album to get a better idea.

Thanks,

KoTa

Update:

I've uploaded a few images to kinda help you with the mood/colour tone and direction of what I want, Also, the script writing (I've uploaded a few examples), do it in white colour (left to right, going little bit upwards), preferably on the bottom of the image, simple, one touch, thin hand writing. Have it fading in size (bigger to smaller) as you get to the end of each word. Just like when you sign something, but have it written in two lines.

The whole image should be deep in colour with sort of a glow effect.

Industry/Entity Type

Painting

Font styles to use
Script

Requirements
Must have
• Name of the album with Script writing,
Should not have
• No paper mosaic art. Image pieced together with cut outs from different sources.

```html
<!DOCTYPE html>
<html lang="en">
<head>
<meta charset="utf-8">
<title>Attic Rivers — Album Cover</title>
<link rel="stylesheet" href="https://fonts.googleapis.com/css2?family=Pinyon+Script&display=swap">
<style>
  :root {
    --frame-lavender: #8f95b5;
    --sky-pale: #eef1f2;
    --sky-haze: #bccbd6;
    --sea-deep: #1f2b4a;
    --sea-navy: #2d3b5e;
    --surf-blue: #7890b0;
    --foam-light: #b4c9d6;
    --foam-white: #e4edf1;
    --sand-rose: #a88e9e;
    --title-white: #ffffff;
  }

  html, body {
    margin: 0;
    padding: 0;
    width: 1200px;
    height: 1200px;
    overflow: hidden;
    background: var(--frame-lavender);
  }

  .cover {
    position: relative;
    width: 1200px;
    height: 1200px;
    background: var(--frame-lavender);
    overflow: hidden;
  }

  .cover__seascape {
    position: absolute;
    left: 101px;
    top: 101px;
    width: 996px;
    height: 996px;
    background: linear-gradient(
      to bottom,
      var(--sky-pale) 0%,
      var(--sky-haze) 19%,
      var(--sea-navy) 20.5%,
      var(--sea-deep) 34%,
      var(--sea-navy) 40%,
      var(--surf-blue) 47%,
      var(--foam-light) 56%,
      var(--foam-light) 68%,
      var(--foam-white) 82%,
      var(--foam-light) 91%,
      var(--sand-rose) 100%
    );
  }

  .cover__title {
    position: absolute;
    left: 0;
    top: 0;
    width: 1200px;
    height: 1200px;
    margin: 0;
    font-family: "Pinyon Script", cursive;
    font-weight: 400;
    color: var(--title-white);
    line-height: 1;
  }

  .cover__title-line {
    position: absolute;
    display: block;
    white-space: nowrap;
    transform-origin: left bottom;
    transform: rotate(-4deg);
  }

  .cover__title-line--first {
    left: 70px;
    top: 240px;
    font-size: 290px;
  }

  .cover__title-line--second {
    left: 290px;
    top: 520px;
    font-size: 260px;
  }
</style>
</head>
<body>
  <main class="cover">
    <div class="cover__seascape" role="img" aria-label="Soft-focus photograph of ocean waves breaking onto a beach under a pale evening sky"></div>
    <h1 class="cover__title">
      <span class="cover__title-line cover__title-line--first">Attic</span>
      <span class="cover__title-line cover__title-line--second">Rivers</span>
    </h1>
  </main>
</body>
</html>
```